Velimo Ventures Logo and Business Card Design

We already have the rough logo shape (however please make the lines on the logo much thicker so a dark background is not required to see it) . see photos uploaded.
It needs to be refined with color and digitized and then have a front and back business card layout done.
The services are high vibration healing support through a therapy and feng shui service offering. We want people to Feel Happiness, Feel Prosperity and Feel Peace. (the back of the card would have these phrases on it) So a warm, calm and peaceful feeling card.
We would like the card to use the logo provided (with thicker lines and color added) but below the graphic please use the name "Velimo Ventures" NOT Velimo.
We also would like to use the colors in the colorized matrix shown in photos (gold and purple) but on the lighter side. Thanks for your time!

Front of Card should include: Logo, with Company Name: Velimo Ventures as part of logo, Name: Mara Donne email: mara@velimo.example web: www.velimo.example mobile: 555.018.2946 at bottom of front list Family Constellation | Feng Shui

Back of Card should have the logo and the following listed vertically:

PERSONAL | BUSINESS (Larger size then smaller bullet items below)
*Find Happiness
*Find Prosperity
*Find Peace

Target Market(s)

Target market is both business and personal

Contact Information for Business Card

Front of Card should include: Logo, with Company Name: Velimo Ventures as part of logo, Name: Mara Donne email: mara@velimo.example web: www.velimo.example mobile: 555.018.2946 at bottom of front list Family Constellation | Feng Shui ++++ Back of Card should have the logo and the following listed vertically: PERSONAL | BUSINESS (Larger size then smaller bullet items below) *Find Happiness *Find Prosperity *Find Peace

Font styles to use
Sans Serif

Colors

Designer to choose colors to be used in the design.

Requirements
Nice to have
• Nice light contrast color for the back of card background
Should not have
• No dark colored background on Card.

```html
<!DOCTYPE html>
<html lang="en">
<head>
<meta charset="utf-8">
<title>Velimo Ventures — Business Card</title>
<link rel="stylesheet" href="https://fonts.googleapis.com/css2?family=Courgette&family=Marcellus&family=Montserrat:wght@400;500&family=Lora:wght@400&display=swap">
<style>
  :root {
    --stage: #ababab;
    --card: #ffffff;
    --purple: #8e4a94;
    --purple-soft: #dcb6dd;
    --gold: #b8974a;
    --gold-soft: #efe4b8;
    --grey-text: #7d7d7d;
    --rule: #c8c8c8;
  }
  * { margin: 0; padding: 0; box-sizing: border-box; }
  html, body { width: 1200px; height: 1000px; overflow: hidden; }
  body { background: var(--stage); position: relative; }

  .card {
    position: absolute;
    left: 294px;
    width: 613px;
    height: 352px;
    background: var(--card);
    border-radius: 24px;
    overflow: hidden;
  }
  .card--front { top: 95px; }
  .card--back { top: 535px; }

  /* Wordmark */
  .wordmark {
    position: absolute;
    display: flex;
    align-items: center;
    gap: 12px;
    font-family: "Marcellus", serif;
    color: var(--purple);
    white-space: nowrap;
  }
  .wordmark__dot {
    border-radius: 50%;
    background: var(--purple-soft);
    flex: none;
  }
  .card--front .wordmark {
    left: 52px; top: 130px;
    flex-direction: column;
    gap: 16px;
    width: 220px;
    font-size: 30px;
    text-align: center;
  }
  .card--front .wordmark__dot { width: 56px; height: 56px; }
  .card--back .wordmark {
    left: 98px; top: 96px;
    font-size: 24px;
  }
  .card--back .wordmark__dot { width: 34px; height: 34px; }

  /* Front contact block */
  .holder-name {
    position: absolute;
    left: 306px; top: 92px;
    font-family: "Courgette", cursive;
    font-size: 31px;
    color: var(--purple);
  }
  .contact-list {
    position: absolute;
    left: 306px; top: 146px;
    list-style: none;
    font-family: "Montserrat", sans-serif;
    color: var(--grey-text);
  }
  .contact-list li {
    display: flex;
    align-items: center;
    gap: 8px;
    height: 26px;
    font-size: 17.5px;
  }
  .contact-list li.contact--phone { font-size: 20px; font-weight: 500; height: 30px; }
  .contact-list svg { width: 12px; height: 12px; flex: none; fill: var(--purple); }

  .divider {
    position: absolute;
    left: 51px; right: 51px; top: 296px;
    border-top: 1px solid var(--rule);
  }
  .services {
    position: absolute;
    left: 0; right: 0; top: 305px;
    text-align: center;
    font-family: "Marcellus", serif;
    font-size: 17px;
    letter-spacing: 1.2px;
    color: var(--purple);
  }

  /* Back */
  .back-decor {
    position: absolute;
    right: 0; top: 0;
    width: 400px; height: 352px;
    background: radial-gradient(ellipse at 85% 45%, rgba(220,182,221,0.55) 0%, rgba(239,228,184,0.45) 45%, rgba(255,255,255,0) 75%);
  }
  .audience {
    position: absolute;
    left: 75px; top: 173px;
    font-family: "Marcellus", serif;
    font-size: 20px;
    letter-spacing: 2.5px;
    color: var(--purple);
  }
  .promises {
    position: absolute;
    left: 96px; top: 202px;
    width: 220px;
    list-style: none;
    text-align: center;
    font-family: "Lora", serif;
    font-size: 25px;
    line-height: 32px;
    color: var(--gold);
  }
</style>
</head>
<body>

  <section class="card card--front" aria-label="Front of business card">
    <div class="wordmark">
      <span class="wordmark__dot" aria-hidden="true"></span>
      <span class="wordmark__name">Velimo Ventures</span>
    </div>

    <h1 class="holder-name">Mara Donne</h1>
    <ul class="contact-list">
      <li class="contact--email">
        <svg viewBox="0 0 12 12" aria-hidden="true"><path d="M0 2h12v8H0z M0 2l6 4 6-4" fill="var(--purple)"/><path d="M1 3l5 3.3L11 3" stroke="#fff" stroke-width="1" fill="none"/></svg>
        mara@velimo.example
      </li>
      <li class="contact--web">
        <svg viewBox="0 0 12 12" aria-hidden="true"><circle cx="6" cy="6" r="5.5"/><path d="M0.5 6h11M6 0.5v11M2 3h8M2 9h8" stroke="#fff" stroke-width="0.8" fill="none"/><ellipse cx="6" cy="6" rx="2.4" ry="5.5" stroke="#fff" stroke-width="0.8" fill="none"/></svg>
        www.velimo.example
      </li>
      <li class="contact--phone">
        <svg viewBox="0 0 12 12" aria-hidden="true"><rect x="2.5" y="0" width="7" height="12" rx="1.2"/><rect x="3.7" y="1.5" width="4.6" height="8" fill="#fff"/></svg>
        555.018.2946
      </li>
    </ul>

    <div class="divider"></div>
    <p class="services">FAMILY CONSTELLATION | FENG SHUI</p>
  </section>

  <section class="card card--back" aria-label="Back of business card">
    <div class="back-decor" role="img" aria-label="Faint large brand mark decoration in soft gold and lilac"></div>

    <div class="wordmark">
      <span class="wordmark__dot" aria-hidden="true"></span>
      <span class="wordmark__name">Velimo Ventures</span>
    </div>

    <p class="audience">PERSONAL | BUSINESS</p>
    <ul class="promises">
      <li>*Find Happiness</li>
      <li>*Find Prosperity</li>
      <li>*Find Peace</li>
    </ul>
  </section>

</body>
</html>
```